Maple Hollow Comets

We are a travel softball organization based in Central IL. Girls are 8-14 yrs old. Looking for a modern website that is easily updated. Our current website is at www.maplehollowcomets.com. I want a tab for each team, 10U, 12U, 14U. I need a tab for pics. A tab for sponsors. A tap for files we have uploaded. And a about tab.

```html
<!DOCTYPE html>
<html lang="en">
<head>
<meta charset="utf-8">
<title>Maple Hollow Comets</title>
<link href="https://fonts.googleapis.com/css2?family=Poppins:wght@300;400;500;600&family=Roboto:wght@400;500;700&family=Yellowtail&display=swap" rel="stylesheet">
<style>
:root{
  --red:#e0232b;
  --red-dark:#b8151c;
  --black:#111;
  --ink:#222;
  --muted:#666;
  --grey:#ececec;
  --line:#ddd;
  --white:#fff;
  --blue:#3b5998;
  --doc:#2b5aa8;
  --pdf:#e0232b;
  --xls:#1f8f3c;
}
*{margin:0;padding:0;box-sizing:border-box}
html,body{width:1200px;height:4813px;overflow:hidden}
body{font-family:"Poppins",sans-serif;color:var(--ink);background:var(--white);position:relative}
section,header,footer{position:absolute;left:0;width:1200px}
.abs{position:absolute}
.btn{position:absolute;display:flex;align-items:center;justify-content:center;background:var(--black);color:var(--white);font:500 19px "Roboto",sans-serif;text-transform:uppercase;border-radius:4px;letter-spacing:.5px}
.photo{position:absolute}
h2.title{position:absolute;font:400 44px "Roboto",sans-serif;text-transform:uppercase;letter-spacing:.5px}
h2.title span{color:var(--red)}
.lorem{font-size:14px;line-height:24px;color:var(--muted)}

/* header */
.site-header{top:0;height:135px;background:var(--white)}
.brand{left:64px;top:28px;display:flex;align-items:center;gap:12px;font:600 26px "Poppins",sans-serif;color:var(--ink);width:300px;line-height:1.05}
.brand i{width:26px;height:26px;border-radius:50%;background:var(--red);flex:none}
.follow{right:64px;top:8px;display:flex;align-items:center;gap:10px;font:500 17px "Roboto",sans-serif;color:var(--red)}
.follow i{width:30px;height:30px;border-radius:50%;background:var(--black)}
.nav{left:360px;top:64px;display:flex;gap:28px;align-items:center;font:500 17px "Roboto",sans-serif;text-transform:uppercase;color:var(--ink)}
.nav .on{background:var(--black);color:var(--white);padding:14px 22px;border-radius:3px}

/* hero */
.hero{top:135px;height:545px;overflow:hidden}
.hero-text{right:77px;top:90px;text-align:right;color:var(--white)}
.hero-text .script{font:400 78px/80px "Yellowtail",cursive}
.hero-text .script.small{font-size:62px;line-height:66px}
.hero-text p{font:italic 400 16px/27px "Poppins",sans-serif;width:520px;margin:22px 0 0 auto}
.hero .btn{right:77px;top:369px;width:170px;height:58px}

/* welcome */
.welcome{top:680px;height:443px;text-align:center}
.ornament{left:560px;top:32px;width:80px;height:76px;border-radius:50%;background:radial-gradient(circle,#e8e8e8,#fff)}
.welcome h2.title{left:0;width:1200px;top:120px}
.welcome .lead{position:absolute;left:0;width:1200px;top:183px;font-size:15px;color:var(--ink)}
.welcome .lorem{position:absolute;left:130px;width:940px;top:222px;font-size:13px}
.welcome .btn{left:520px;top:328px;width:160px;height:54px}

/* teams */
.team{height:363px;background:var(--grey)}
.team .photo{top:0;width:600px;height:363px}
.team .badge{top:136px;width:90px;height:90px;border-radius:50%;background:var(--white);border:6px solid var(--grey)}
.team h3{position:absolute;top:52px;font:400 40px "Roboto",sans-serif}
.team h3 span{color:var(--red)}
.team .lorem{position:absolute;top:112px;width:470px;font-size:13px;line-height:23px}
.team .btn{top:237px;width:168px;height:56px}
.team.left .photo{left:0}.team.left .badge{left:555px}
.team.left h3,.team.left .lorem{left:668px}.team.left .btn{left:658px}
.team.right .photo{left:600px}.team.right .badge{left:555px}
.team.right h3,.team.right .lorem{left:80px}.team.right .btn{left:80px}

/* files */
.files{top:2218px;height:639px;text-align:center}
.files h2.title{left:0;width:1200px;top:50px}
.files .lead{position:absolute;left:220px;width:760px;top:116px;font-size:13px;line-height:22px;color:var(--ink)}
.file-band{position:absolute;left:154px;top:212px;width:892px;height:292px;background:var(--grey)}
.file{position:absolute;top:212px;width:300px;height:292px}
.file.featured{top:170px;left:443px;width:311px;height:366px;background:var(--white);box-shadow:0 4px 18px rgba(0,0,0,.18)}
.file svg{position:absolute;left:50%;margin-left:-44px;top:52px}
.file.featured svg{top:64px}
.file .name{position:absolute;left:0;width:100%;top:212px;font-size:17px;color:var(--ink)}
.file.featured .name{top:255px}
.file .dl{position:absolute;left:0;width:100%;top:290px;font-size:17px;color:var(--red)}
.files .btn{left:523px;top:527px;width:154px;height:55px}

/* testimonial */
.testimonial{top:2857px;height:481px;background:linear-gradient(180deg,#d91f27,#c0181f 60%,#d62229);color:var(--white);text-align:center}
.testimonial h2.title{left:0;width:1200px;top:60px;color:var(--black)}
.testimonial h2.title span{color:var(--white)}
.quote-mark{position:absolute;left:560px;top:136px;width:80px;height:80px;border-radius:50%;border:3px solid var(--white);display:flex;align-items:center;justify-content:center;font:700 64px/1 "Roboto",sans-serif;padding-top:26px}
.testimonial p{position:absolute;left:130px;width:940px;top:235px;font-size:15px;line-height:30px}
.arrow{position:absolute;top:320px;font:300 40px "Poppins",sans-serif;color:rgba(255,255,255,.7)}
.avatar{position:absolute;left:490px;top:310px;width:82px;height:82px;border-radius:50%;background:linear-gradient(135deg,#d8b6a0,#6c4a3a);border:3px solid var(--white)}
.client{position:absolute;left:588px;top:325px;text-align:left;font-size:16px;line-height:24px}

/* about + social */
.about{top:3338px;height:578px}
.about h2.title{left:80px;top:38px}
.about .lead{position:absolute;left:80px;width:520px;top:120px;font-size:14px;line-height:25px;color:var(--ink)}
.about .lorem{position:absolute;left:80px;width:520px;top:185px;font-size:13px;line-height:23px}
.board{position:absolute;left:80px;top:318px;border-collapse:collapse;font-size:13px}
.board td{height:26px;padding:0}
.board td:first-child{width:152px;color:var(--ink);font-weight:500}
.board td:nth-child(2){width:60px;color:var(--muted)}
.board td:last-child{color:var(--muted)}
.social h2.title{left:712px;top:38px}
.widget{position:absolute;left:712px;top:112px;width:367px;height:402px;border:1px solid var(--line);background:var(--white);font-family:"Roboto",sans-serif}
.widget .bar{height:58px;background:var(--blue);color:var(--white);font-size:26px;padding:12px 16px}
.widget .tab{height:40px;border-bottom:1px solid var(--line);font-size:15px;padding:10px 16px;color:var(--ink)}
.widget .page{position:absolute;left:14px;top:120px;width:337px;height:90px;border-bottom:1px solid var(--line)}
.widget .avatar-sq{position:absolute;left:0;top:0;width:60px;height:60px;background:var(--red)}
.widget .pname{position:absolute;left:72px;top:6px;font-size:17px;font-weight:700}
.widget .psub{position:absolute;left:72px;top:30px;font-size:13px;color:var(--muted)}
.widget .f-sq{position:absolute;right:6px;top:10px;width:30px;height:30px;background:var(--blue);border-radius:4px}
.widget .post{position:absolute;left:14px;top:222px;width:337px;font-size:13px;line-height:20px}
.widget .post b{font-weight:700}
.widget .post em{color:var(--red);font-style:normal}
.widget .strip{position:absolute;left:14px;top:300px;width:337px;height:60px;background:linear-gradient(90deg,#8ba2c0,#c9c4bd,#9fb28a,#c7a7a0)}
.widget .foot{position:absolute;left:14px;right:14px;top:370px;display:flex;justify-content:space-between;font-size:13px}

/* gallery */
.gallery{top:3916px;height:514px;background:linear-gradient(180deg,#d3222a,#b9161d)}
.gallery h2.title{left:0;width:1200px;top:64px;text-align:center;color:var(--black)}
.gallery h2.title span{color:var(--white)}
.gallery .photo{top:154px;width:300px;height:248px}
.gallery .zoom{position:absolute;left:116px;top:178px;width:42px;height:42px;border-radius:50%;background:var(--red);display:flex;align-items:center;justify-content:center}
.g-arrows{position:absolute;left:548px;top:420px;display:flex;gap:8px}
.g-arrows span{width:46px;height:46px;border:2px solid var(--white);color:var(--white);display:flex;align-items:center;justify-content:center;font:500 24px "Roboto",sans-serif}
.g-arrows span:first-child{background:var(--red-dark)}

/* footer */
.site-footer{top:4430px;height:327px}
.f-brand{left:80px;top:60px;width:220px;font:600 26px/1.1 "Poppins",sans-serif;display:flex;gap:12px;align-items:center}
.f-brand i{width:26px;height:26px;border-radius:50%;background:var(--red);flex:none}
.f-social{left:178px;top:218px;width:44px;height:44px;border-radius:50%;background:var(--red)}
.f-col h4{font:500 19px "Roboto",sans-serif;text-transform:uppercase;letter-spacing:1px;margin-bottom:16px}
.links{left:343px;top:30px}
.links ul{list-style:none;font-size:14px;line-height:22px;color:var(--muted)}
.links li::before{content:"";display:inline-block;width:7px;height:7px;border-radius:50%;background:var(--ink);margin-right:14px;vertical-align:middle}
.news{left:603px;top:30px;width:250px}
.news p{font-size:13px;line-height:21px;color:var(--muted)}
.news .input{margin-top:16px;height:40px;border:1px solid var(--line);font-size:13px;color:var(--muted);padding:10px 12px}
.news .btn{position:relative;margin-top:18px;width:155px;height:53px}
.photos{left:873px;top:30px}
.photos .grid{display:grid;grid-template-columns:repeat(3,88px);gap:8px}
.photos .grid div{height:86px}
.photos .more{margin-top:14px;text-align:right;font:500 14px "Roboto",sans-serif;color:var(--red);text-decoration:underline}
.copyright{top:4757px;height:56px;background:var(--red);color:var(--white);font-size:13px;display:flex;align-items:center;justify-content:center}
</style>
</head>
<body>

<header class="site-header">
  <div class="abs brand"><i></i>Maple Hollow Comets</div>
  <div class="abs follow">Follow Us On : <i></i></div>
  <nav class="abs nav">
    <span class="on">Home</span><span>About</span><span>10 U</span><span>12 U</span><span>14 U</span><span>Gallery</span><span>Sponsors</span><span>Files</span><span>Contact</span>
  </nav>
</header>

<section class="hero">
  <div class="photo" role="img" aria-label="Team photo of the girls softball squad in red and white uniforms on a field" style="left:0;top:0;width:1200px;height:545px;background:linear-gradient(120deg,#6f8a5a,#a9a9a0 40%,#c7403e 70%)"></div>
  <svg class="abs" style="left:0;top:0" width="1200" height="545" viewBox="0 0 1200 545">
    <polygon points="760,0 1200,0 1200,545 560,545" fill="#d11f27" opacity=".93"/>
    <polygon points="720,0 780,0 580,545 520,545" fill="#111"/>
    <polygon points="1200,0 1200,40 1160,0" fill="#111"/>
  </svg>
  <div class="abs hero-text">
    <div class="script">Maple Hollow</div>
    <div class="script small">Comets</div>
    <p>Maple Hollow Comets is a Girls Travel Softball Organization Based Out Of Alder Falls, But With Players From All Over Harlow County</p>
  </div>
  <span class="btn">Join Us Now</span>
</section>

<section class="welcome">
  <div class="abs ornament" role="img" aria-label="Flaming softball emblem"></div>
  <h2 class="title">Welcome to <span>Maple Hollow Comets</span></h2>
  <p class="lead">Maple Hollow Comets is a Girls Travel Softball Organization Based Out Of Alder Falls, But With Players From All Over Harlow County</p>
  <p class="lorem">Lorem Ipsum is simply dummy text of the printing and typesetting industry. Lorem Ipsum has been the industry's standard dummy text ever since the 1500s, when an unknown printer took a galley of type and scrambled it to make a type specimen book. It has survived not only five centuries, but also the leap into electronic typesetting, remaining essentially unchanged.</p>
  <span class="btn">Know More</span>
</section>

<section class="team left" style="top:1123px">
  <div class="photo" role="img" aria-label="10U team group photo on the field" style="background:linear-gradient(135deg,#7c9a5e,#b7584f 55%,#e3e0da)"></div>
  <div class="abs badge"></div>
  <h3>10 <span>U</span></h3>
  <p class="lorem">Lorem Ipsum is simply dummy text of the printing and typesetting industry. Lorem Ipsum has been the industry's standard dummy text ever since the 1500s, when an unknown printer took a galley of type and scrambled it to make a type specimen book.</p>
  <span class="btn">Know More</span>
</section>

<section class="team right" style="top:1486px">
  <div class="photo" role="img" aria-label="12U team group photo in front of trees" style="background:linear-gradient(135deg,#6d8c4f,#a7b3a3 40%,#c55a55)"></div>
  <div class="abs badge"></div>
  <h3>12 <span>U</span></h3>
  <p class="lorem">Lorem Ipsum is simply dummy text of the printing and typesetting industry. Lorem Ipsum has been the industry's standard dummy text ever since the 1500s, when an unknown printer took a galley of type and scrambled it to make a type specimen book.</p>
  <span class="btn">Know More</span>
</section>

<section class="team left" style="top:1852px">
  <div class="photo" role="img" aria-label="14U team group photo on the field" style="background:linear-gradient(135deg,#7e9464,#c8504b 50%,#d8d2cb)"></div>
  <div class="abs badge"></div>
  <h3>14 <span>U</span></h3>
  <p class="lorem">Lorem Ipsum is simply dummy text of the printing and typesetting industry. Lorem Ipsum has been the industry's standard dummy text ever since the 1500s, when an unknown printer took a galley of type and scrambled it to make a type specimen book.</p>
  <span class="btn">Know More</span>
</section>

<section class="files">
  <h2 class="title">Our <span>Files</span></h2>
  <p class="lead">Download Our Files For Schedule , Meeting , Budget And May More Information About Maple Hollow Comets</p>
  <div class="file-band"></div>
  <div class="file" style="left:154px">
    <svg width="88" height="120" viewBox="0 0 88 120"><path d="M10 16h50l20 20v80H10z" fill="#fff" stroke="#ccc" stroke-width="2"/><rect x="0" y="6" width="64" height="26" fill="var(--doc)"/><text x="32" y="25" fill="#fff" font-family="Roboto,sans-serif" font-size="16" text-anchor="middle">DOCX</text><rect x="24" y="52" width="42" height="5" fill="var(--doc)"/><rect x="24" y="66" width="42" height="5" fill="var(--doc)"/><rect x="24" y="80" width="30" height="5" fill="var(--doc)"/></svg>
    <div class="name">Organization Bylaws</div>
  </div>
  <div class="file featured">
    <svg width="88" height="120" viewBox="0 0 88 120"><path d="M10 16h50l20 20v80H10z" fill="#fff" stroke="#ccc" stroke-width="2"/><rect x="0" y="6" width="64" height="26" fill="var(--pdf)"/><text x="32" y="25" fill="#fff" font-family="Roboto,sans-serif" font-size="16" text-anchor="middle">PDF</text><rect x="24" y="52" width="42" height="5" fill="var(--pdf)"/><rect x="24" y="66" width="42" height="5" fill="var(--pdf)"/><rect x="24" y="80" width="30" height="5" fill="var(--pdf)"/></svg>
    <div class="name">2017 12U Schedule</div>
    <div class="dl">Download</div>
  </div>
  <div class="file" style="left:746px">
    <svg width="88" height="120" viewBox="0 0 88 120"><path d="M10 16h50l20 20v80H10z" fill="#fff" stroke="#ccc" stroke-width="2"/><rect x="0" y="6" width="64" height="26" fill="var(--xls)"/><text x="32" y="25" fill="#fff" font-family="Roboto,sans-serif" font-size="16" text-anchor="middle">XLS</text><rect x="24" y="52" width="42" height="5" fill="var(--xls)"/><rect x="24" y="66" width="42" height="5" fill="var(--xls)"/><rect x="24" y="80" width="30" height="5" fill="var(--xls)"/></svg>
    <div class="name">2017 Budget</div>
  </div>
  <span class="btn">View All</span>
</section>

<section class="testimonial">
  <h2 class="title">What our <span>client say</span></h2>
  <div class="quote-mark">&ldquo;</div>
  <p>&ldquo; Lorem Ipsum is simply dummy text of the printing and typesetting industry. Lorem Ipsum has been the industry's standard dummy text ever since the 1500s, when an unknown printer took a galley of type and scrambled it to make. &rdquo;</p>
  <span class="arrow" style="left:424px">&lsaquo;</span>
  <span class="arrow" style="left:764px">&rsaquo;</span>
  <div class="avatar" role="img" aria-label="Client portrait"></div>
  <div class="client">CLIENT NAME<br>something.com</div>
</section>

<section class="about">
  <h2 class="title">About <span>Us</span></h2>
  <p class="lead">Maple Hollow Comets is a Girls Travel Softball Organization Based Out Of Alder Falls, But With Players From All Over Harlow County</p>
  <p class="lorem">Lorem Ipsum is simply dummy text of the printing and typesetting industry. Lorem Ipsum has been the industry's standard dummy text ever since the 1500s, when an unknown printer took a galley of type and scrambled it to make a type specimen book. It has survived not only five centuries, but also the leap.</p>
  <table class="board">
    <tr><td>President</td><td>:</td><td>Dana Whitfield</td></tr>
    <tr><td>Vice President</td><td>:</td><td>Rob Kessler</td></tr>
    <tr><td>Treasurer</td><td>:</td><td>Lena Ortiz</td></tr>
    <tr><td>Secretary</td><td>:</td><td>Kara Mills</td></tr>
    <tr><td>Club Teams Director</td><td>:</td><td>Erin Kessler</td></tr>
    <tr><td>Parent at large</td><td>:</td><td>Paul Ortiz</td></tr>
    <tr><td>Operations Director</td><td>:</td><td>Rob Kessler</td></tr>
  </table>
  <div class="social">
    <h2 class="title">Follow us <span>Pagebook</span></h2>
    <div class="widget">
      <div class="bar">Pagebook</div>
      <div class="tab">Pagebook @COMETS</div>
      <div class="page">
        <div class="avatar-sq"></div>
        <div class="pname">COMETS</div>
        <div class="psub">MAPLE HOLLOW</div>
        <div class="f-sq"></div>
      </div>
      <div class="post"><b>Maple Hollow Comets</b> added 16 new photos to the album <b>Comets vs. Riverton</b>.<br><em>13 May at 20:45</em></div>
      <div class="strip" role="img" aria-label="Row of game photo thumbnails"></div>
      <div class="foot"><span>Embed</span><span>View on Pagebook</span></div>
    </div>
  </div>
</section>

<section class="gallery">
  <h2 class="title">Our <span>Gallery</span></h2>
  <div class="photo" role="img" aria-label="Player portrait in team jersey" style="left:0;background:linear-gradient(135deg,#4f3b34,#9a7f70)"></div>
  <div class="photo" role="img" aria-label="Batter at the plate" style="left:300px;background:linear-gradient(135deg,#6d8a4c,#b7a48d 60%,#c13a36)"></div>
  <div class="photo" role="img" aria-label="Players celebrating on the field" style="left:600px;background:linear-gradient(135deg,#8a9e75,#c7b9a5 50%,#d44b45)"></div>
  <div class="photo" role="img" aria-label="Team huddle near the dugout" style="left:900px;background:linear-gradient(135deg,#a9a391,#c84a44 55%,#7f8d66)"></div>
  <div class="zoom"><svg width="22" height="22" viewBox="0 0 22 22"><circle cx="9" cy="9" r="6.5" fill="none" stroke="#fff" stroke-width="2.5"/><path d="M14 14l6 6" stroke="#fff" stroke-width="2.5"/></svg></div>
  <div class="g-arrows"><span>&lsaquo;</span><span>&rsaquo;</span></div>
</section>

<footer class="site-footer">
  <div class="abs f-brand"><i></i>Maple Hollow Comets</div>
  <div class="abs f-social"></div>
  <div class="abs f-col links">
    <h4>Usefull Links</h4>
    <ul><li>Home</li><li>About</li><li>10 U</li><li>12 U</li><li>14 U</li><li>Gallery</li><li>Sponsors</li><li>Files</li><li>Contact</li></ul>
  </div>
  <div class="abs f-col news">
    <h4>Newsletter</h4>
    <p>Would you like to receive exclusive access to articles, white papers and our regular monthly newsletter?</p>
    <div class="input">Enter Email Id</div>
    <span class="btn">Subscribe</span>
  </div>
  <div class="abs f-col photos">
    <h4>Photos</h4>
    <div class="grid">
      <div role="img" aria-label="Team photo thumbnail" style="background:linear-gradient(135deg,#7a8f5e,#c44a44)"></div>
      <div role="img" aria-label="Game action thumbnail" style="background:linear-gradient(135deg,#b9a690,#cc3d39)"></div>
      <div role="img" aria-label="Players thumbnail" style="background:linear-gradient(135deg,#8c9c78,#d8d2c9)"></div>
      <div role="img" aria-label="Dugout thumbnail" style="background:linear-gradient(135deg,#c44a44,#7b8b65)"></div>
      <div role="img" aria-label="Field thumbnail" style="background:linear-gradient(135deg,#6f8a52,#bcb5a8)"></div>
      <div role="img" aria-label="Celebration thumbnail" style="background:linear-gradient(135deg,#d2504a,#a49985)"></div>
    </div>
    <div class="more">VIEW ALL</div>
  </div>
</footer>

<div class="abs copyright" style="left:0;width:1200px">&copy;MAPLE HOLLOW COMETS - 2017 All Rights Reserved</div>

</body>
</html>
```